" MINHA EMPRESA É PRESTADORA DE SERVIÇOS PARA ORGÃOS PUBLICOS, TRABALHAMOS EM VARIOS SEGMENTOS, SERVIÇOS DE REFORMA EM GERAL, FORNECIMENTO DE MATERIAL DE CONSTRUÇÃO, REALIZAÇÃO DE EVENTOS, DETRE VARIOS OUTROS MAIS. "

```html
<!DOCTYPE html>
<html lang="pt-BR">
<head>
<meta charset="utf-8">
<title>Brevanta — Pasta institucional</title>
<link href="https://fonts.googleapis.com/css2?family=Exo+2:wght@500;800&family=Arimo:wght@700&display=swap" rel="stylesheet">
<style>
  :root {
    --brand-blue: #1c6496;
    --brand-yellow: #f7c224;
    --paper: #ffffff;
    --backdrop: #e9e7e3;
    --tagline: #7e8a93;
    --ghost-light: rgba(255,255,255,0.07);
    --ghost-dark: rgba(28,100,150,0.05);
  }
  html, body {
    margin: 0;
    width: 1200px;
    height: 1200px;
    overflow: hidden;
    background: var(--backdrop);
  }
  .folder {
    position: absolute;
    left: 60px;
    top: 252px;
    width: 1040px;
    height: 752px;
    box-shadow: 0 6px 18px rgba(0,0,0,0.18);
  }
  .folder__back {
    position: absolute;
    left: 0; top: 0;
    width: 516px; height: 100%;
    background: var(--brand-blue);
    overflow: hidden;
  }
  .folder__front {
    position: absolute;
    left: 516px; top: 0;
    width: 524px; height: 100%;
    background: var(--paper);
    overflow: hidden;
  }
  .folder__flap {
    position: absolute;
    left: 0; top: 0;
    width: 516px; height: 84px;
  }
  .folder__band {
    position: absolute;
    left: 0; bottom: 0;
    width: 100%; height: 14px;
    background: var(--brand-yellow);
  }
  .ghost-name {
    position: absolute;
    font-family: "Exo 2", sans-serif;
    font-weight: 800;
    font-size: 150px;
    letter-spacing: -4px;
    white-space: nowrap;
    line-height: 1;
  }
  .folder__back .ghost-name { left: 20px; top: 330px; color: var(--ghost-light); }
  .folder__front .ghost-name { left: 110px; top: 510px; color: var(--ghost-dark); }

  .brand {
    position: absolute;
    text-align: center;
    font-family: "Exo 2", sans-serif;
  }
  .brand__mark {
    display: inline-block;
    background: var(--brand-yellow);
  }
  .brand__name {
    font-weight: 800;
    line-height: 1;
  }
  .brand__tagline {
    font-weight: 500;
    text-transform: uppercase;
    line-height: 1;
  }

  .brand--cover {
    left: 0; width: 524px; top: 568px;
    color: var(--brand-blue);
  }
  .brand--cover .brand__mark { width: 26px; height: 26px; margin-bottom: 14px; }
  .brand--cover .brand__name { font-size: 50px; letter-spacing: 2px; }
  .brand--cover .brand__tagline { font-size: 19px; letter-spacing: 5px; color: var(--tagline); margin-top: 8px; }

  .brand--back {
    left: 0; width: 516px; top: 818px;
    color: var(--paper);
  }
  .brand--back .brand__mark { width: 14px; height: 14px; margin-bottom: 6px; }
  .brand--back .brand__name { font-size: 30px; letter-spacing: 1px; }
  .brand--back .brand__tagline { font-size: 12px; letter-spacing: 3px; margin-top: 4px; }

  .contact {
    position: absolute;
    left: 0; width: 516px; top: 925px;
    margin: 0;
    text-align: center;
    font-family: "Arimo", sans-serif;
    font-weight: 700;
    font-size: 10px;
    line-height: 13px;
    color: var(--paper);
    font-style: normal;
  }
</style>
</head>
<body>
  <main class="folder">
    <section class="folder__back">
      <svg class="folder__flap" viewBox="0 0 516 84" aria-hidden="true">
        <polygon points="0,0 516,0 516,84 48,84" fill="var(--brand-yellow)"/>
      </svg>
      <div class="ghost-name" aria-hidden="true">BREVANTA</div>
      <div class="brand brand--back">
        <span class="brand__mark"></span>
        <div class="brand__name">BREVANTA</div>
        <div class="brand__tagline">Comércio e Serviços</div>
      </div>
      <address class="contact">
        www.brevanta.com.br<br>
        Rua das Acácias, 120 Centro - Cidade - Estado - Cep. 00.000-000<br>
        (11) 4000-2000<br>
        contato@brevanta.com.br
      </address>
      <div class="folder__band"></div>
    </section>

    <section class="folder__front">
      <div class="brand brand--cover">
        <span class="brand__mark"></span>
        <div class="brand__name">BREVANTA</div>
        <div class="brand__tagline">Comércio e Serviços</div>
      </div>
      <div class="ghost-name" aria-hidden="true">BREVANTA</div>
      <div class="folder__band"></div>
    </section>
  </main>
</body>
</html>
```